Harrowmere Lodge Sign

Harrowmere Lodge is a lake resort in Willowmere, OR
This resort used to have 66 units however the resort was sold in sections. I own the part of the resort that has all the amenities listed on the attached file. We need an updated sign and also billboard.
On a sign like this should be include a phone number?

```html
<!DOCTYPE html>
<html lang="en">
<head>
<meta charset="utf-8">
<title>Harrowmere Lodge Sign</title>
<link href="https://fonts.googleapis.com/css2?family=Poppins:wght@600;700&display=swap" rel="stylesheet">
<style>
  :root {
    --navy: #0b3570;
    --ink: #18407a;
    --sky-top: #36bcf1;
    --sky-mid: #8fd5f2;
    --sky-low: #d6f0f8;
    --white: #ffffff;
    --pin: #f7e23a;
  }
  * { margin: 0; padding: 0; box-sizing: border-box; }
  html, body {
    width: 1200px; height: 941px; overflow: hidden;
    background: var(--white);
    font-family: "Poppins", Arial, sans-serif;
  }
  .sign {
    position: absolute; left: 93px; top: 101px;
    width: 1025px; height: 723px; overflow: hidden;
    background: linear-gradient(180deg, var(--sky-top) 0%, var(--sky-mid) 40%, var(--sky-low) 62%, #f6fcfd 70%, var(--white) 75%);
  }
  .brand-top {
    position: absolute; left: 50px; top: 100px; width: 401px;
    color: var(--white); font-weight: 600; font-size: 40px;
    text-align: center; line-height: 1.1; white-space: nowrap;
  }
  .locale {
    position: absolute; left: 558px; top: 48px;
    display: flex; align-items: center; gap: 8px;
    color: var(--ink); font-weight: 700; font-size: 23px; white-space: nowrap;
  }
  .url-band { position: absolute; left: 506px; top: 91px; width: 519px; height: 72px; }
  .url {
    position: absolute; left: 506px; top: 91px; width: 519px; height: 72px;
    display: flex; align-items: center; padding-left: 41px;
    color: var(--white); font-weight: 700; font-size: 28.5px; letter-spacing: 0.2px;
  }
  .amenities { list-style: none; position: absolute; top: 0; left: 0; }
  .amenities li {
    position: absolute; display: flex; align-items: center; gap: 16px;
    color: var(--ink); font-weight: 700; font-size: 25px; white-space: nowrap;
    transform: translateY(-50%);
  }
  .amenities svg { width: 25px; height: 25px; flex: none; }
  .col-left li { left: 61px; }
  .col-right li { left: 575px; }
  .brand-bottom {
    position: absolute; left: 564px; top: 508px; width: 428px;
    color: var(--navy); font-weight: 700; font-size: 52px; line-height: 1.05;
    text-align: center;
  }
  .contact-bar {
    position: absolute; left: 0; bottom: 0; width: 100%; height: 67px;
    background: var(--navy); color: var(--white);
    font-weight: 600; font-size: 38px;
  }
  .contact { position: absolute; top: 0; height: 67px; display: flex; align-items: center; gap: 11px; white-space: nowrap; }
  .contact.phone { left: 52px; }
  .contact.address { left: 558px; }
  .contact svg { width: 39px; height: 39px; flex: none; }
</style>
</head>
<body>
<main class="sign">
  <div class="brand-top">Harrowmere Lodge</div>

  <div class="locale">
    <svg width="30" height="40" viewBox="0 0 30 40" aria-hidden="true">
      <path d="M15 2C8 2 3 7 3 14c0 9 12 24 12 24s12-15 12-24C27 7 22 2 15 2z" fill="var(--pin)"/>
      <circle cx="15" cy="14" r="5" fill="var(--sky-mid)"/>
    </svg>
    LAKE RESORT IN WILLOWMERE, OR
  </div>

  <svg class="url-band" viewBox="0 0 519 72" preserveAspectRatio="none" aria-hidden="true">
    <path d="M30 4 C120 0 300 6 420 2 C470 1 500 4 519 6 L519 66 C470 70 420 68 330 70 C220 72 110 66 40 68 C10 68 0 52 2 36 C4 16 12 5 30 4z" fill="var(--navy)"/>
  </svg>
  <div class="url">www.harrowmerelodge.com</div>

  <ul class="amenities col-left">
    <li style="top:223px"><svg viewBox="0 0 25 25"><path d="M2 13l7 9L23 3" fill="none" stroke="var(--ink)" stroke-width="3"/></svg>DIRECT LAKE ACCESS</li>
    <li style="top:266px"><svg viewBox="0 0 25 25"><path d="M2 13l7 9L23 3" fill="none" stroke="var(--ink)" stroke-width="3"/></svg>SWIM DECKS</li>
    <li style="top:311px"><svg viewBox="0 0 25 25"><path d="M2 13l7 9L23 3" fill="none" stroke="var(--ink)" stroke-width="3"/></svg>SLIP RENTALS</li>
    <li style="top:353px"><svg viewBox="0 0 25 25"><path d="M2 13l7 9L23 3" fill="none" stroke="var(--ink)" stroke-width="3"/></svg>BOAT RENTALS</li>
    <li style="top:396px"><svg viewBox="0 0 25 25"><path d="M2 13l7 9L23 3" fill="none" stroke="var(--ink)" stroke-width="3"/></svg>INDOOR POOL</li>
    <li style="top:439px"><svg viewBox="0 0 25 25"><path d="M2 13l7 9L23 3" fill="none" stroke="var(--ink)" stroke-width="3"/></svg>GOLF CARTS</li>
    <li style="top:479px"><svg viewBox="0 0 25 25"><path d="M2 13l7 9L23 3" fill="none" stroke="var(--ink)" stroke-width="3"/></svg>PONTOON BOATS</li>
    <li style="top:516px"><svg viewBox="0 0 25 25"><path d="M2 13l7 9L23 3" fill="none" stroke="var(--ink)" stroke-width="3"/></svg>KAYAK – PADDLEBOARDS</li>
    <li style="top:558px"><svg viewBox="0 0 25 25"><path d="M2 13l7 9L23 3" fill="none" stroke="var(--ink)" stroke-width="3"/></svg>1-3 BEDROOM</li>
    <li style="top:605px"><svg viewBox="0 0 25 25"><path d="M2 13l7 9L23 3" fill="none" stroke="var(--ink)" stroke-width="3"/></svg>DINNIG HALL</li>
  </ul>

  <ul class="amenities col-right">
    <li style="top:222px"><svg viewBox="0 0 25 25"><path d="M2 13l7 9L23 3" fill="none" stroke="var(--ink)" stroke-width="3"/></svg>GAME ROOM</li>
    <li style="top:266px"><svg viewBox="0 0 25 25"><path d="M2 13l7 9L23 3" fill="none" stroke="var(--ink)" stroke-width="3"/></svg>CHILDREN'S ACTIVITIES</li>
    <li style="top:307px"><svg viewBox="0 0 25 25"><path d="M2 13l7 9L23 3" fill="none" stroke="var(--ink)" stroke-width="3"/></svg>PET FRIENDLY</li>
    <li style="top:350px"><svg viewBox="0 0 25 25"><path d="M2 13l7 9L23 3" fill="none" stroke="var(--ink)" stroke-width="3"/></svg>GIFT STORE</li>
    <li style="top:391px"><svg viewBox="0 0 25 25"><path d="M2 13l7 9L23 3" fill="none" stroke="var(--ink)" stroke-width="3"/></svg>OUTDOOR GAMES</li>
    <li style="top:435px"><svg viewBox="0 0 25 25"><path d="M2 13l7 9L23 3" fill="none" stroke="var(--ink)" stroke-width="3"/></svg>FAMILY REUNION</li>
  </ul>

  <div class="brand-bottom">Harrowmere<br>Lodge</div>

  <footer class="contact-bar">
    <div class="contact phone">
      <svg viewBox="0 0 40 40" aria-hidden="true">
        <circle cx="20" cy="20" r="20" fill="var(--white)"/>
        <path d="M14 10c1-1 2-1 3 0l3 4c1 1 0 2-1 3l-1 1c1 3 4 6 7 7l1-1c1-1 2-2 3-1l4 3c1 1 1 2 0 3l-2 2c-2 2-8 0-13-5S10 16 12 12z" fill="var(--navy)"/>
      </svg>
      (541) 555-0186
    </div>
    <div class="contact address">
      <svg viewBox="0 0 40 40" aria-hidden="true">
        <circle cx="20" cy="20" r="20" fill="var(--white)"/>
        <path d="M20 8c-5 0-9 4-9 9 0 7 9 16 9 16s9-9 9-16c0-5-4-9-9-9z" fill="var(--navy)"/>
        <circle cx="20" cy="17" r="3.5" fill="var(--white)"/>
      </svg>
      28 Birchwood Lane
    </div>
  </footer>
</main>
</body>
</html>
```